Business Card Design

We require a business card design for a law firm, our signature colours are maroon and cream. Our slogan is "From our family to yours", we would like the cards to be professional however feminine at the same time.

Industry/Entity Type

Business

Contact Information for Business Card

Helena Brackett & Associates Lawyers & Conveyancers, Helena Brackett LL.B. Principal Solicitor, 17 Quillon Street, Marrowdale NSW 2190

Logo styles of interest
Emblem Logo
Abstract Logo
Wordmark Logo

```html
<!DOCTYPE html>
<html lang="en">
<head>
<meta charset="utf-8">
<title>Helena Brackett &amp; Associates – Business Card</title>
<link rel="stylesheet" href="https://fonts.googleapis.com/css2?family=Open+Sans:wght@400&display=swap">
<style>
  :root {
    --maroon: #6c0e2f;
    --maroon-deep: #4f0820;
    --maroon-light: #7d1a3d;
    --bar: #8c1c42;
    --bar-accent: #a8264f;
    --cream: #f7f0c8;
    --rule: #c9607d;
    --frame: #9a8a8f;
  }
  * { margin: 0; padding: 0; box-sizing: border-box; }
  html, body {
    width: 1200px; height: 695px; overflow: hidden;
    background: #ffffff;
  }
  .card {
    position: relative;
    width: 1200px; height: 695px;
    overflow: hidden;
    font-family: "Open Sans", "Segoe UI", Arial, sans-serif;
    color: var(--cream);
    background: radial-gradient(ellipse at 30% 45%, var(--maroon-light) 0%, var(--maroon) 45%, var(--maroon-deep) 100%);
    border: 2px solid var(--frame);
    box-shadow: inset 0 0 0 2px rgba(255,255,255,0.15), inset 0 0 40px rgba(0,0,0,0.35);
  }
  .text-shadow { text-shadow: 1px 2px 2px rgba(0,0,0,0.45); }
  .identity {
    position: absolute; right: 74px; top: 98px;
    text-align: right;
  }
  .identity__name { font-size: 45px; line-height: 54px; }
  .identity__title { font-size: 40px; line-height: 56px; }
  .identity__rule {
    position: absolute; left: 735px; top: 234px;
    width: 378px; height: 4px;
    background: linear-gradient(90deg, transparent, var(--rule) 25%, var(--bar) 70%, transparent);
    opacity: 0.85;
  }
  .firm-mark {
    position: absolute; left: 160px; top: 160px;
    width: 280px; height: 230px;
    display: flex; align-items: center; justify-content: center;
    font-size: 30px; text-align: center;
  }
  .firm-name {
    position: absolute; left: 36px; top: 440px;
    width: 560px; text-align: center;
    font-size: 32px; line-height: 46px;
  }
  .address {
    position: absolute; right: 74px; top: 433px;
    text-align: right;
    font-size: 34px; line-height: 51px;
  }
  .footer-bar {
    position: absolute; left: 0; top: 627px;
    width: 642px; height: 19px;
    background: var(--bar);
  }
  .footer-square {
    position: absolute; top: 627px; height: 19px;
    background: var(--bar);
  }
  .footer-square--one { left: 652px; width: 24px; }
  .footer-square--two { left: 687px; width: 23px; background: var(--bar-accent); }
</style>
</head>
<body>
  <div class="card">
    <div class="identity text-shadow">
      <div class="identity__name">Helena Brackett LL.B.</div>
      <div class="identity__title">Principal Solicitor</div>
    </div>
    <div class="identity__rule"></div>

    <div class="firm-mark text-shadow">Helena Brackett</div>

    <div class="firm-name text-shadow">
      Helena Brackett &amp; Associates<br>
      Lawyers &amp; Conveyancers
    </div>

    <div class="address text-shadow">
      17 Quillon Street<br>
      Marrowdale NSW 2190
    </div>

    <div class="footer-bar"></div>
    <div class="footer-square footer-square--one"></div>
    <div class="footer-square footer-square--two"></div>
  </div>
</body>
</html>
```